Modern, pro female massage business needs business card design

We are a boutique, pro women's sports and remedial massage studio based in Singapore - we have a logo already (see attached image) and need to design a business card that reflects an elegant, modern and feminine feel using this logo.

We are focussed on a very local market and need to give a professional yet warm feeling.

Details for the card include (layout of your choice):

Tamsin Vale
Call, SMS or WhatsApp: 9183 6027
Email: bluefennel@mailbox-example.com
Address: The Harbourview on Talbot
72 Talbot Road, Westmere, Singapore

To incorporate the QRAB logo (www.qrabglobal.co.uk) would be appreciated - see attached file.

Industry/Entity Type

Massage

Requirements
Nice to have
• We like the idea of using an embossed style card. Solid colour on the reverse - embossed on the front; four colour printing is okay.
Should not have
• It should not be uber 'girly girl' if that makes any sense. The logo is already colourful

```html
<!DOCTYPE html>
<html lang="en">
<head>
<meta charset="utf-8">
<title>rosethistle – business card</title>
<link rel="stylesheet" href="https://fonts.googleapis.com/css2?family=Open+Sans:wght@300;400;700&display=swap">
<style>
  :root {
    --canvas: #e9e9e9;
    --card-white: #ffffff;
    --rose-light: #f0505e;
    --rose-mid: #d4415a;
    --rose-deep: #8c1a3c;
    --brand: #c0334f;
    --ink-light: #ffffff;
    --shadow: rgba(0, 0, 0, 0.22);
  }
  html, body {
    margin: 0;
    padding: 0;
    width: 1200px;
    height: 1000px;
    overflow: hidden;
    background: var(--canvas);
    font-family: "Open Sans", Arial, sans-serif;
  }
  .stage {
    position: relative;
    width: 1200px;
    height: 1000px;
  }
  .card {
    position: absolute;
    border-radius: 24px;
    box-shadow: 6px 8px 12px var(--shadow);
    overflow: hidden;
  }
  .card--front {
    left: 346px;
    top: 146px;
    width: 533px;
    height: 307px;
    background: linear-gradient(135deg, var(--rose-light) 0%, var(--rose-light) 12%, var(--rose-mid) 42%, var(--rose-deep) 82%, var(--rose-deep) 100%);
    color: var(--ink-light);
    border: 1px solid #5a2030;
    box-sizing: border-box;
  }
  .card--back {
    left: 344px;
    top: 531px;
    width: 534px;
    height: 310px;
    background: var(--card-white);
  }
  .brand-name {
    position: absolute;
    margin: 0;
    font-weight: 700;
    letter-spacing: -1.5px;
    line-height: 1;
    white-space: nowrap;
  }
  .brand-tagline {
    position: absolute;
    margin: 0;
    font-weight: 400;
    line-height: 1;
    white-space: nowrap;
  }
  .card--front .brand-name {
    left: 245px;
    top: 82px;
    font-size: 40px;
    color: var(--ink-light);
  }
  .card--front .brand-tagline {
    left: 246px;
    top: 120px;
    font-size: 12.5px;
    color: var(--ink-light);
  }
  .card--back .brand-name {
    left: 106px;
    top: 120px;
    font-size: 58px;
    color: var(--brand);
  }
  .card--back .brand-tagline {
    left: 108px;
    top: 181px;
    font-size: 18px;
    color: var(--brand);
  }
  .holder-name {
    position: absolute;
    left: 98px;
    top: 159px;
    margin: 0;
    font-size: 17px;
    font-weight: 400;
    line-height: 1;
  }
  .contact-list {
    position: absolute;
    left: 246px;
    top: 160px;
    margin: 0;
    padding: 0;
    list-style: none;
    font-size: 15px;
    font-weight: 300;
    line-height: 20.5px;
  }
  .contact-list li {
    display: flex;
    align-items: center;
    white-space: nowrap;
  }
  .contact-icon {
    width: 13px;
    height: 13px;
    margin-right: 2px;
    flex: none;
  }
  .contact-letter {
    font-weight: 700;
    font-size: 13px;
    width: 13px;
    margin-right: 2px;
  }
  .address {
    position: absolute;
    left: 97px;
    top: 232px;
    margin: 0;
    font-size: 13px;
    font-weight: 300;
    letter-spacing: -0.6px;
    white-space: nowrap;
  }
</style>
</head>
<body>
<main class="stage">
  <section class="card card--front" aria-label="Card front">
    <p class="brand-name">rosethistle</p>
    <p class="brand-tagline">Remedial and sports massage</p>
    <h1 class="holder-name">Tamsin Vale</h1>
    <ul class="contact-list">
      <li>
        <svg class="contact-icon" viewBox="0 0 16 16" aria-hidden="true">
          <path fill="#fff" d="M4.2 1.5l2 3.1c.3.4.2.9-.1 1.2l-1 1c.8 1.7 2.2 3.1 3.9 3.9l1-1c.3-.3.8-.4 1.2-.1l3.1 2c.4.3.5.8.2 1.2l-1.2 1.5c-.4.5-1.1.7-1.7.5C6.8 13.4 2.6 9.2 1.2 4.4c-.2-.6 0-1.3.5-1.7L3 1.3c.4-.3.9-.2 1.2.2z"/>
        </svg>9183 6027
      </li>
      <li>
        <svg class="contact-icon" viewBox="0 0 16 16" aria-hidden="true">
          <rect x="1" y="4" width="14" height="9" fill="#fff"/>
          <path d="M1 4l7 5 7-5" fill="none" stroke="#b53050" stroke-width="1.2"/>
        </svg>tamsin@softstone-example.net
      </li>
      <li><span class="contact-letter">w</span>bluefennel@mailbox-example.com</li>
    </ul>
    <p class="address">The Harbourview on Talbot, 72 Talbot Road, Westmere, Singapore</p>
  </section>

  <section class="card card--back" aria-label="Card back">
    <p class="brand-name">rosethistle</p>
    <p class="brand-tagline">Remedial and sports massage</p>
  </section>
</main>
</body>
</html>
```